Business card

creative business card for newly created national firm that specializes in high-density storage for retail markets. Looking for creativity and overall theme that will differentiate from others in this unique niche ...essentially a design that will provide instant recognition as we develop our identity in the marketplace. possible initial thoughts are attached with logo separately

Industry/Entity Type

Retail

```html
<!DOCTYPE html>
<html lang="en">
<head>
<meta charset="utf-8">
<title>Compact Stock Systems – Business Card</title>
<link rel="stylesheet" href="https://fonts.googleapis.com/css2?family=Lato:ital,wght@0,400;0,700;0,900;1,400&display=swap">
<style>
  :root {
    --sky: #addcf5;
    --ink: #0b0b0b;
    --deep: #1e4f66;
    --mark: #2f8cb9;
    --ghost: #f1f3f6;
    --paper: #ffffff;
  }
  html, body {
    margin: 0;
    padding: 0;
    width: 1200px;
    height: 720px;
    overflow: hidden;
    background: var(--paper);
  }
  .card {
    position: relative;
    width: 1200px;
    height: 720px;
    background: var(--paper);
    font-family: "Lato", sans-serif;
  }
  .brand-panel {
    position: absolute;
    left: 162px;
    top: 232px;
    width: 399px;
    height: 472px;
    background: var(--sky);
  }
  .brand-square {
    position: absolute;
    left: 222px;
    top: 70px;
    width: 260px;
    height: 260px;
    background: var(--mark);
  }
  .brand-name {
    position: absolute;
    left: 186px;
    top: 440px;
    margin: 0;
    font-family: "Lato", sans-serif;
    font-weight: 400;
    font-size: 56px;
    line-height: 64px;
    letter-spacing: 1px;
    color: var(--deep);
    text-transform: uppercase;
  }
  .brand-name span { display: block; }
  .contact-panel {
    position: absolute;
    left: 664px;
    top: 0;
    width: 399px;
    height: 230px;
    background: var(--sky);
    text-align: center;
  }
  .person-name {
    margin: 0;
    position: absolute;
    left: 0;
    right: 0;
    top: 140px;
    font-weight: 900;
    font-size: 40px;
    letter-spacing: 1px;
    color: var(--ink);
  }
  .phone {
    margin: 0;
    position: absolute;
    left: 0;
    right: 0;
    top: 192px;
    font-weight: 400;
    font-size: 30px;
    color: var(--ink);
  }
  .ghost-square {
    position: absolute;
    left: 728px;
    top: 290px;
    width: 260px;
    height: 260px;
    background: var(--ghost);
  }
  .tagline {
    position: absolute;
    left: 668px;
    top: 340px;
    margin: 0;
    font-style: italic;
    font-size: 41px;
    color: var(--deep);
  }
  .website {
    position: absolute;
    left: 672px;
    top: 617px;
    margin: 0;
    font-style: italic;
    font-size: 24px;
    color: var(--ink);
  }
</style>
</head>
<body>
  <div class="card">
    <div class="brand-panel"></div>
    <div class="brand-square"></div>
    <h1 class="brand-name"><span>Compact</span><span>Stock</span><span>Systems</span></h1>

    <div class="contact-panel">
      <p class="person-name">DANA MERROW</p>
      <p class="phone">855-SHELF-PRO</p>
    </div>

    <div class="ghost-square"></div>
    <p class="tagline">Innovate your space</p>
    <p class="website">www.compactstocksystems.com</p>
  </div>
</body>
</html>
```